General Contractors need a new Crisp updated Card Design

We need a new business card design for our company of 25 years based in Toronto call Holvaster Building Inc. : Our goal is to be the leading commercial contractors in Toronto by providing exceptional value to our clients. We work very hard to deliver professional, quality, service in conjunction with consistent price competitiveness to all of our clients on every single project.

Target Market(s)

Design & Build Clients

Industry/Entity Type

Construction Company

Contact Information for Business Card

Address:
18 North Tamlin Glen Road, Unit 57, Marbrook Vale, ON, K7T 2R9
Office: 905-218-5937

Holvasters Logo
Employee Job Description
Employee Cell Phone #
Employee Email
www.holvaster-example.com

Colors

Designer to choose colors to be used in the design.

Requirements
Must have
• Quote Company Saying:
• "Professional. Quality. Service."
Nice to have
• New Crisp up to date look. simple & fresh ( Not to Busy)
Should not have
• NO BLUE PRINTS ON THE BUSINESS CARDS

```html
<!DOCTYPE html>
<html lang="en">
<head>
<meta charset="utf-8">
<title>Holvaster Building Inc. – Business Cards</title>
<link rel="stylesheet" href="https://fonts.googleapis.com/css2?family=Roboto:wght@400;500;700&family=Roboto+Condensed:wght@700&display=swap">
<style>
  :root {
    --brand-green: #00766b;
    --stage-grey: #dddee0;
    --card-white: #ffffff;
    --ink: #222222;
    --rule: #333333;
  }
  * { box-sizing: border-box; margin: 0; padding: 0; }
  html, body { width: 1200px; height: 770px; overflow: hidden; }
  body {
    background: var(--stage-grey);
    font-family: "Roboto", Arial, sans-serif;
    color: var(--ink);
    position: relative;
  }
  .card {
    position: absolute;
    width: 499px;
    height: 284px;
    background: var(--card-white);
    box-shadow: 0 1px 4px rgba(0,0,0,0.18);
    overflow: hidden;
  }
  .card--front { left: 350px; top: 80px; background: var(--brand-green); }
  .card--back-a { left: 80px; top: 405px; }
  .card--back-b { left: 620px; top: 405px; }

  /* Wordmark (text-only company name with a plain square) */
  .wordmark { position: absolute; display: flex; align-items: center; gap: 9px; }
  .wordmark__square { width: 48px; height: 48px; background: var(--brand-green); flex: none; }
  .wordmark__name {
    font-weight: 500; font-size: 20px; line-height: 1.1;
    color: var(--brand-green); letter-spacing: 0.2px;
  }
  .card--front .wordmark { left: 161px; top: 193px; gap: 12px; }
  .card--front .wordmark__square { width: 70px; height: 70px; background: none; border: 2px solid #fff; }
  .card--front .wordmark__name { color: #fff; font-size: 31px; line-height: 1.08; }
  .card--back-a .wordmark { left: 253px; top: 22px; }
  .card--back-b .wordmark { left: 263px; top: 22px; }

  /* Tagline band */
  .tagline-band {
    position: absolute; left: 0; top: 22px; width: 245px; height: 48px;
    background: var(--brand-green); color: #fff;
    font-family: "Roboto Condensed", Arial, sans-serif; font-weight: 700; font-size: 16px;
    display: flex; align-items: center; padding-left: 29px;
  }
  .tagline {
    position: absolute; left: 263px; top: 246px;
    color: var(--brand-green); font-size: 16px; font-weight: 400;
  }

  .employee { position: absolute; }
  .employee__name { font-weight: 700; font-size: 15.5px; letter-spacing: -0.2px; }
  .employee__title { font-size: 12.5px; margin-top: 1px; }
  .card--back-a .employee { left: 29px; top: 155px; }
  .card--back-b .employee { left: 23px; top: 128px; }
  .accent-bar { position: absolute; left: 0; top: 117px; width: 9px; height: 51px; background: var(--brand-green); }

  .divider { position: absolute; left: 29px; top: 204px; width: 441px; height: 1px; background: var(--rule); }

  .contact-list { position: absolute; list-style: none; font-size: 12.6px; line-height: 17.7px; }
  .contact-list li { display: flex; align-items: center; gap: 4px; white-space: nowrap; }
  .contact-list svg { width: 10px; height: 10px; fill: var(--brand-green); flex: none; }
  .card--back-a .contact-list { left: 29px; top: 211px; }
  .card--back-b .contact-list { left: 263px; top: 149px; }

  .address { position: absolute; font-size: 12.6px; line-height: 17.7px; font-style: normal; }
  .card--back-a .address { right: 29px; top: 211px; text-align: right; }
  .card--back-b .address { left: 263px; top: 102px; }
</style>
</head>
<body>

<section class="card card--front" aria-label="Card front">
  <div class="wordmark">
    <span class="wordmark__square"></span>
    <span class="wordmark__name">Holvaster<br>Building Inc.</span>
  </div>
</section>

<section class="card card--back-a" aria-label="Card back, layout A">
  <div class="tagline-band">Professional. Quality. Service.</div>
  <div class="wordmark">
    <span class="wordmark__square"></span>
    <span class="wordmark__name">Holvaster<br>Building Inc.</span>
  </div>
  <div class="employee">
    <div class="employee__name">EMPLOYEE NAME</div>
    <div class="employee__title">TITLE</div>
  </div>
  <div class="divider"></div>
  <ul class="contact-list">
    <li><svg viewBox="0 0 10 10"><path d="M2 0.5l2 2-1 1.2c.6 1.3 1.6 2.3 2.9 2.9l1.2-1 2 2-1.3 1.6C4.4 9.2 0.8 5.6.4 1.8z"/></svg>905-218-5937</li>
    <li><svg viewBox="0 0 10 10"><path d="M2.5 0h5v10h-5zM3.5 1v6.8h3V1zM4.5 8.4h1v0.9h-1z" fill-rule="evenodd"/></svg>123-456-7890</li>
    <li><svg viewBox="0 0 10 10"><path d="M0 1.5h10v7H0zM0.8 2.3L5 5.4l4.2-3.1z" fill-rule="evenodd"/></svg>name@holvaster-example.com</li>
  </ul>
  <address class="address">18 North Tamlin Glen Road, Unit 57<br>Marbrook Vale, ON, K7T 2R9<br>www.holvaster-example.com</address>
</section>

<section class="card card--back-b" aria-label="Card back, layout B">
  <div class="wordmark">
    <span class="wordmark__square"></span>
    <span class="wordmark__name">Holvaster<br>Building Inc.</span>
  </div>
  <div class="accent-bar"></div>
  <div class="employee">
    <div class="employee__name">EMPLOYEE NAME</div>
    <div class="employee__title">TITLE</div>
  </div>
  <address class="address">18 North Tamlin Glen Road Unit 57<br>Marbrook Vale, ON, K7T 2R9</address>
  <ul class="contact-list">
    <li><svg viewBox="0 0 10 10"><path d="M2 0.5l2 2-1 1.2c.6 1.3 1.6 2.3 2.9 2.9l1.2-1 2 2-1.3 1.6C4.4 9.2 0.8 5.6.4 1.8z"/></svg>905-218-5937</li>
    <li><svg viewBox="0 0 10 10"><path d="M2.5 0h5v10h-5zM3.5 1v6.8h3V1zM4.5 8.4h1v0.9h-1z" fill-rule="evenodd"/></svg>123-456-7890</li>
    <li><svg viewBox="0 0 10 10"><path d="M0 1.5h10v7H0zM0.8 2.3L5 5.4l4.2-3.1z" fill-rule="evenodd"/></svg>name@holvaster-example.com</li>
    <li><svg viewBox="0 0 10 10"><circle cx="5" cy="5" r="4.3" fill="none" stroke="#00766b" stroke-width="1"/><path d="M0.7 5h8.6M5 0.7v8.6" stroke="#00766b" stroke-width="0.9"/><ellipse cx="5" cy="5" rx="2" ry="4.3" fill="none" stroke="#00766b" stroke-width="0.9"/></svg>www.holvaster-example.com</li>
  </ul>
  <div class="tagline">Professional. Quality. Service.</div>
</section>

</body>
</html>
```